DuneOrbit Signage Design Project

We need a signage design for our company's new location, we are a GPS tracking and monitoring systems company,

we would like to see signage designs that use colors similar to the company's logo,

Please consider that we will add Arabic words in all Signage,

new photos uploaded...

Target Market(s)

GPS/GPRS tracking and monitoring systems

Industry/Entity Type

Gps

Requirements
Must have
• Large billboard must have out-frame details and some idea related to tracking and navigation systems. (similar to the attached Photo)

1- We need billboard signage,
2- outdoor signage and on-glass signage
3- garage signage,

Nice to have
• logo attached, earth, satellite, location pin, map.

```html
<!DOCTYPE html>
<html lang="en">
<head>
<meta charset="UTF-8">
<title>Garage Sign</title>
<link rel="stylesheet" href="https://fonts.googleapis.com/css2?family=Jost:wght@600&display=swap">
<style>
  :root {
    --sign-red: #e11f26;
    --sign-red-deep: #c8161d;
    --panel-black: #231815;
    --sign-white: #ffffff;
  }
  html, body {
    margin: 0;
    padding: 0;
    overflow: hidden;
    background: #ffffff;
  }
  .garage-sign {
    position: relative;
    width: 1200px;
    height: 250px;
    display: flex;
    overflow: hidden;
    background: var(--sign-red);
  }
  .icon-panel {
    flex: 0 0 270px;
    height: 250px;
    background: var(--panel-black);
  }
  .icon-panel svg {
    display: block;
  }
  .label-area {
    position: relative;
    flex: 1;
    display: flex;
    align-items: center;
    justify-content: center;
  }
  .sign-label {
    margin: 0;
    font-family: "Jost", "Futura", sans-serif;
    font-weight: 600;
    font-size: 118px;
    letter-spacing: 4px;
    color: var(--sign-white);
    line-height: 1;
    position: relative;
    z-index: 1;
    transform: translateY(2px);
  }
  .corner-ring {
    position: absolute;
    right: -45px;
    bottom: -80px;
    width: 240px;
    height: 240px;
    border-radius: 50%;
    border: 10px solid var(--sign-red-deep);
    box-sizing: border-box;
  }
</style>
</head>
<body>
  <div class="garage-sign">
    <div class="icon-panel">
      <svg class="garage-icon" width="270" height="250" viewBox="0 0 270 250" aria-label="Garage icon" role="img">
        <polyline class="garage-roof" points="30,114 135,30 240,114" fill="none" stroke="#ffffff" stroke-width="13" stroke-linejoin="miter"/>
        <g class="car" fill="#ffffff">
          <path d="M96 112 Q100 104 110 104 L160 104 Q170 104 174 112 L186 150 Q198 154 198 168 L198 202 Q198 210 190 210 L80 210 Q72 210 72 202 L72 168 Q72 154 84 150 Z"/>
          <rect x="82" y="200" width="26" height="26" rx="5"/>
          <rect x="162" y="200" width="26" height="26" rx="5"/>
        </g>
        <path class="windshield" d="M108 116 L162 116 L172 148 L98 148 Z" fill="#231815"/>
        <circle class="headlight" cx="94" cy="174" r="9" fill="#231815"/>
        <circle class="headlight" cx="176" cy="174" r="9" fill="#231815"/>
      </svg>
    </div>
    <div class="label-area">
      <h1 class="sign-label">GARAGE</h1>
      <div class="corner-ring" aria-hidden="true"></div>
    </div>
  </div>
</body>
</html>
```